Business Card Design Project for Female Personal Trainer

I need a business card design to appeal to female clients for my personal training and group fitness boot camp business called 'Lumeva Studios'. It should be girly, fun and have an active/healthy pic or figure incorporated into the business name.

Target Market(s)

- Females 20-65yrs

Industry/Entity Type

Training

Font styles to use
Serif
Sans Serif

Colors
e34197
e567a6

Requirements
Must have
• First Side of Business Card Details :

Corin Delph
MASTER PERSONAL TRAINER
Cert III & Cert IV in Fitness
Senior First Aid
Mobile: 0438 507 164
Email: lumeva@quillpost.net
Facebook: Lumeva Studios

* Mobile Personal Training *Individual Sessions *Bootcamp *Weight-loss and Toning

Second Side of Business Card I want to offer a free personal consult:
Something like this:

Need direction with your health & fitness goals?

Call now for your free 1 on 1 Personal Training Session with full consultation

Nice to have
• Have a sub-heading for example:

'Promoting healthy living through fitness & nutrition'

- have the colour pink or blue (to appeal to a female)

- a picture/motif//logo attached (sometimes a picture paints a thousand words)

Should not have
• * picture of a person with big muscles or appeal to a man (I'm training women only)

* should not be busy or crammed up look (if I've added to much info above please just use to your discretion).

```html
<!DOCTYPE html>
<html lang="en">
<head>
<meta charset="UTF-8">
<title>Lumeva Studios – Business Card</title>
<link rel="stylesheet" href="https://fonts.googleapis.com/css2?family=Ubuntu:wght@400;500;700&display=swap">
<style>
  :root {
    --page: #e9ecef;
    --white: #ffffff;
    --ink-blue: #1f67a8;
    --ink-blue-soft: #2b8ccc;
    --band-dark: #1b5c9c;
    --band-light: #3aa3d8;
    --panel-top: #2a88c8;
    --panel-bottom: #174f8c;
    --box: #1d5f9f;
    --list-text: #d8e8f5;
    --muted-text: #b9cfe3;
  }
  * { margin: 0; padding: 0; box-sizing: border-box; }
  html, body {
    width: 1200px; height: 900px; overflow: hidden;
    background: var(--page);
    font-family: "Ubuntu", Arial, sans-serif;
  }
  .canvas {
    position: relative; width: 1200px; height: 900px;
    display: flex; flex-direction: column; align-items: center; justify-content: center; gap: 40px;
  }
  .card {
    position: relative; width: 680px; height: 390px;
    border-radius: 22px; overflow: hidden;
    box-shadow: 0 8px 24px rgba(0,0,0,0.18);
    background: var(--white);
  }
  .card-bg { position: absolute; inset: 0; }

  /* Offer side */
  .offer-headline {
    position: absolute; left: 38px; top: 44px; width: 290px;
    color: var(--ink-blue); font-weight: 700; font-size: 34px; line-height: 1.08;
  }
  .runners {
    position: absolute; left: 150px; top: 200px; width: 230px; height: 170px;
  }
  .offer-box-text {
    position: absolute; right: 28px; top: 18px; width: 300px;
    color: var(--white); font-weight: 700; font-size: 19px; line-height: 1.25; text-align: center;
  }
  .programs {
    position: absolute; left: 400px; top: 140px; width: 260px;
    color: var(--list-text); font-weight: 500; font-size: 16px; line-height: 1.35;
    list-style: none;
  }
  .programs .programs-title { color: var(--white); margin-bottom: 2px; }
  .programs li.item { padding-left: 22px; }
  .programs li.item::before { content: "* "; }

  /* Contact side */
  .identity { position: absolute; left: 36px; top: 110px; }
  .name { color: var(--ink-blue); font-weight: 700; font-size: 44px; line-height: 1; letter-spacing: 0.5px; }
  .title { color: var(--ink-blue); font-weight: 700; font-size: 18px; margin-top: 4px; padding-left: 34px; }
  .creds { color: var(--ink-blue-soft); font-weight: 500; font-size: 16px; text-align: center; margin-top: 6px; line-height: 1.25; }
  .contacts {
    position: absolute; left: 40px; bottom: 32px; list-style: none;
    color: var(--ink-blue-soft); font-weight: 700; font-size: 19px; line-height: 1.3;
  }
  .contacts li { display: flex; align-items: center; gap: 10px; }
  .contacts svg { width: 13px; height: 13px; flex: none; }
  .services {
    position: absolute; right: 30px; top: 40px; width: 280px; list-style: none;
    text-align: right; color: var(--muted-text); font-weight: 700; font-size: 18px; line-height: 1.45;
  }
  .services li.spaced { margin-top: 10px; }
</style>
</head>
<body>
<main class="canvas">

  <!-- Offer side -->
  <section class="card card-offer">
    <svg class="card-bg" viewBox="0 0 680 390" preserveAspectRatio="none" aria-hidden="true">
      <defs>
        <linearGradient id="panelGradA" x1="0" y1="0" x2="1" y2="1">
          <stop offset="0" stop-color="var(--panel-top)"/>
          <stop offset="1" stop-color="var(--panel-bottom)"/>
        </linearGradient>
      </defs>
      <path d="M300 0 Q420 180 360 390 L680 390 L680 0 Z" fill="var(--band-dark)"/>
      <path d="M320 0 Q440 180 380 390 L680 390 L680 0 Z" fill="var(--band-light)"/>
      <path d="M345 0 Q460 180 405 390 L680 390 L680 0 Z" fill="url(#panelGradA)"/>
      <path d="M355 0 L680 0 L680 118 L400 118 Q385 50 355 0 Z" fill="var(--box)"/>
    </svg>
    <h2 class="offer-headline">Need direction with your health &amp; fitness goals?</h2>
    <div class="runners" role="img" aria-label="Silhouettes of two women running and leaping"
         style="background: radial-gradient(ellipse at center, #8a9099 0%, #c9cdd2 60%, rgba(255,255,255,0) 80%); border-radius: 40px;"></div>
    <p class="offer-box-text">Call now for your free 1 on 1 Personal Training Session with full consultation</p>
    <ul class="programs">
      <li class="programs-title">Fitness Programs:</li>
      <li class="item">Weight loss consults</li>
      <li class="item">female specific training</li>
      <li class="item">body sculpting</li>
      <li class="item">HIIT</li>
      <li class="item">pre-post natal</li>
    </ul>
  </section>

  <!-- Contact side -->
  <section class="card card-contact">
    <svg class="card-bg" viewBox="0 0 680 390" preserveAspectRatio="none" aria-hidden="true">
      <defs>
        <linearGradient id="panelGradB" x1="0" y1="0" x2="1" y2="1">
          <stop offset="0" stop-color="var(--panel-top)"/>
          <stop offset="1" stop-color="var(--panel-bottom)"/>
        </linearGradient>
      </defs>
      <path d="M320 0 Q420 210 230 390 L680 390 L680 0 Z" fill="var(--band-dark)"/>
      <path d="M340 0 Q440 210 255 390 L680 390 L680 0 Z" fill="var(--band-light)"/>
      <path d="M362 0 Q462 210 282 390 L680 390 L680 0 Z" fill="url(#panelGradB)"/>
    </svg>
    <div class="identity">
      <h1 class="name">Corin Delph</h1>
      <p class="title">MASTER PERSONAL TRAINER</p>
      <p class="creds">Cert III &amp; Cert IV in Fitness<br>Senior First Aid</p>
    </div>
    <ul class="contacts">
      <li>
        <svg viewBox="0 0 16 16" aria-hidden="true"><path d="M3 1l3 3-1.5 2c1 2 2.5 3.5 4.5 4.5L11 9l3 3-2 3C6 14 2 10 1 3z" fill="var(--ink-blue)"/></svg>
        0438 507 164
      </li>
      <li>
        <svg viewBox="0 0 16 16" aria-hidden="true"><rect x="1" y="3" width="14" height="10" fill="var(--ink-blue)"/><path d="M1 3l7 6 7-6" stroke="#fff" stroke-width="1.5" fill="none"/></svg>
        lumeva@quillpost.net
      </li>
      <li>
        <svg viewBox="0 0 16 16" aria-hidden="true"><rect x="1" y="1" width="14" height="14" rx="2" fill="var(--ink-blue)"/></svg>
        Lumeva Studios
      </li>
    </ul>
    <ul class="services">
      <li>Mobile Personal Training</li>
      <li>Group Sessions</li>
      <li>Individual Sessions</li>
      <li>Bootcamp</li>
      <li class="spaced">Boxing for strength and fitness</li>
      <li class="spaced">Weight-loss and Toning</li>
      <li>General Fitness</li>
    </ul>
  </section>

</main>
</body>
</html>
```